Brightline Office Systems needs an "Explainer Flyer"

One of the main problems we are having in trying to convey the major difference in our service is how we do it is somewhat wordy and is hard to separate ourselves.

Our service model is VERY different from our competitors and is VERY disruptive.

This flyer should be more of an informational flyer as opposed to a flyer designed to sell something. This may also need to be a two page 8.5" X 11" flyer. The design we are looking for could best be described as an "Explainer Flyer". Something like an explainer video only on paper. The flyer should show explain the differences between Brightline Office Systems and our competitors AND the psychology of how we arrived at our model.

Here in plain English is how we explain our service to prospects when we are face to face with them. You can see right away how wordy it is even if we just focus on the bare minimum to convey the actual difference in what we do.

One of the most frustrating things about service in the copier industry is expectations. If you call in for service via the phone, when will someone take "ownership" of your problem? Even if the average on-site response time is 2-4 hours? The ownership of your problem does not transfer to the tech until the tech arrives.

Worse yet is when you place a service request online. When will someone call you and take ownership of your problem? Not just dispatch the call but take ownership of your problem? Have you ever filled out a form online requesting information or help then waited hours or even days for a response?

At Brightline Office Systems, we took a long hard look at the traditional service model of the copier industry and discovered that the main issue with copier service was the expectations of transfer of ownership with regards to the actual problem. When we asked our customers what was most important, response time to take over ownership was 1st and response time to be on site was second.

Understanding this new sociology of service, allowed us to change the game in regards to service. In October of 2017, we started answering online requests for service in less than 5 minutes! In addition, we no longer use dispatchers or office personnel to be the first responders. Now we have 2nd level technicians responding to the initial request. This has been a huge success in ways that we didn't even expect. 1st, 40% of all service requests are solved over the phone or internet by the responding 2nd level tech. Secondly, when a 2nd level tech assesses the problem on the first call, he gives the user the expectation that he has taken ownership of the problem and the expectation of the exact ETA of when the tech will be on site. Lastly, since the first responder is a 2nd level tech, the onsite tech is much more informed on what parts to bring or what are to focus on first. This has led to a very high first visit fix rate of 93.7% compared the industry average of just 68.4%.

For conversations regarding our ability to service anywhere in the US. (Likely to be page two)

We changed our name to Brightline Office Systems in March of 2016 to more accurately describe what we do and where we do it.

All Copier companies who provide sales and service all over the US do it the same flawed way. if they have a company that needs copiers and service in multiple states or cities will have to negotiate separate service contracts with other copier companies in each respective state or city.
There are three major problems with doing so.

1. Not all copier companies offer the same level of service in regards to response times, friendliness or quality of repairs. It varies greatly from state to state and city to city and there is very little command and control from the home copier company if something does not go well.

2. Conflicting Incentives of priorities. The local copier company will almost always service their own customers first when resources are strained. They do so because of the value of their own customers are much higher than their contracted accounts.

3. Service history data is fractured. Service history is actionable data that is important in the relationship between the copier vendor and the customer. In order to make changes in service, fleet size or redistributing resources, the service history is a vital tool.

At Brightline Office Systems, we worked for almost three years to solve this problem. We solved this problem by doing the following.

1. We eliminated the need to create separate side contracts with other copier companies by accumulating a vast database of contracted freelance copier technicians AND IT technicians.

2. We then created a program where the freelance techs wear a Brightline Office Systems shirt when performing Brightline Office Systems repairs.

3. The contracted tech is vetted and trained by Brightline Office Systems to a minimum service quality level.

4. Most importantly, all of our customers nationwide receive the same 5 minute response time on the transfer of ownership of their problem.

5. Command and control of all tech and service calls are retained by Brightline Office Systems nationwide!

One of the biggest advantages of developing this model is that our concentration of contracted freelance techs for any zip code is at least 5-1 over the local vendor. For example, any single copier company in Jacksonville Florida might have 2-3 technicians available at any given time. Brightline Office Systems has 26 contracted technicians in a 25-mile radius of Jacksonville Florida.

This is a much more efficient, and properly incented service delivery model. It is a very disruptive methodology for delivering a kind of service experience that has not changed in 50 years.

Target Market(s)

Copier Industry

Industry/Entity Type

Business Service

Colors

Designer to choose colors to be used in the design.

Requirements
Must have
• All information is in the Project Description.
Nice to have
Should not have

```html
<!DOCTYPE html>
<html lang="en">
<head>
<meta charset="utf-8">
<title>Brightline Office Systems – Explainer Flyer</title>
<link href="https://fonts.googleapis.com/css2?family=Oswald:wght@400;500;600&family=Lato:ital,wght@0,400;0,700;0,900;1,400;1,700&display=swap" rel="stylesheet">
<style>
  :root{
    --navy:#25225e;
    --navy-deep:#1c1a4d;
    --red:#a5161f;
    --ink:#2b2b33;
    --grey-light:#f3f3f5;
    --grey-mid:#dcdce2;
    --stage:#d7d7db;
    --white:#ffffff;
  }
  *{box-sizing:border-box;margin:0;padding:0}
  html,body{width:1200px;height:902px;overflow:hidden}
  body{background:var(--stage);font-family:"Lato",Arial,sans-serif;color:var(--ink);position:relative}

  .page{position:absolute;top:88px;width:560px;height:725px;background:var(--white);overflow:hidden;box-shadow:0 4px 14px rgba(0,0,0,.18)}
  .page--front{left:30px}
  .page--back{left:610px}

  .photo{position:absolute}
  .swoosh{position:absolute;left:0;width:560px}

  .brand{position:absolute;display:flex;align-items:center;gap:6px;font-family:"Oswald",Arial,sans-serif;font-weight:500;color:var(--navy);white-space:nowrap}
  .brand__dot{width:12px;height:12px;border-radius:50%;background:var(--red);flex:none}

  .heading{font-family:"Oswald",Arial,sans-serif;text-transform:uppercase;line-height:1.1}
  .red{color:var(--red)}
  .navy{color:var(--navy)}

  p,li{font-size:7.4px;line-height:1.38}

  /* front */
  .front-title{position:absolute;left:270px;top:118px;width:282px;text-align:center}
  .front-title__lead{font-size:20px;color:var(--red);font-weight:500}
  .front-title__box{display:inline-block;margin:4px 0;background:var(--navy);color:var(--white);font-size:14.5px;padding:4px 8px;font-weight:500}
  .front-title__sub{font-size:12.5px;color:var(--red);font-weight:500}

  .col{position:absolute}
  .col--left{left:0;top:318px;width:282px;padding:0 16px 0 16px}
  .col--right{left:282px;top:300px;width:278px;height:425px;background:linear-gradient(180deg,#f7f7f9,#e6e6ea)}

  .section-head{display:flex;gap:8px;align-items:flex-start;margin-bottom:6px}
  .section-head__mark{flex:none;width:12px;height:16px;margin-left:-16px;background:linear-gradient(90deg,var(--navy) 0 60%,var(--white) 60% 75%,var(--red) 75%)}
  .section-head__text{font-size:9px;font-weight:700;text-transform:uppercase;color:var(--navy-deep);line-height:1.3}
  .bullets{list-style:none;margin:0 0 6px 4px}
  .bullets li{position:relative;padding-left:14px;margin-bottom:4px;color:var(--red);font-style:italic}
  .bullets li::before{content:"";position:absolute;left:0;top:2px;width:6px;height:6px;border-radius:50%;background:var(--navy)}
  .col--left p{margin-bottom:10px}

  .right-intro{padding:14px 14px 8px 16px;font-size:8.6px;font-weight:700;text-transform:uppercase;color:var(--navy-deep);line-height:1.3}
  .date-banner{margin-left:-8px;background:var(--navy);color:var(--white);padding:8px 12px 9px;font-family:"Oswald",Arial,sans-serif;text-transform:uppercase}
  .date-banner__top{font-size:14px;font-weight:500}
  .date-banner__mid{font-size:9.5px;color:#e2333d;margin:3px 0}
  .date-banner__end{font-size:13px;font-weight:500}
  .point{display:flex;gap:10px;padding:10px 14px 0 0}
  .point__mark{flex:none;width:24px;height:15px;background:linear-gradient(90deg,var(--navy) 0 70%,var(--grey-light) 70% 80%,var(--red) 80%)}
  .result{padding:16px 16px 0 16px;font-size:10.5px;font-style:italic;font-weight:700;color:var(--red);line-height:1.35}

  .footer-call{position:absolute;display:flex;align-items:center;gap:10px;color:var(--white)}
  .footer-call__label{font-size:8.5px;color:#e2333d;text-transform:uppercase}
  .footer-call__number{font-size:14px;font-weight:700;letter-spacing:.5px}

  /* back */
  .back-left{position:absolute;left:0;top:222px;width:188px;height:440px;background:linear-gradient(180deg,#ececef,#fafafa)}
  .back-left__head{padding:6px 14px 10px;text-align:center}
  .back-left__head span{display:block}
  .back-left__head .l1{font-size:13px;color:var(--ink)}
  .back-left__head .l2{font-size:16.5px;color:var(--red);font-weight:500;margin-top:2px}
  .name-box{background:var(--navy);padding:12px 12px 14px;text-align:center;font-family:"Oswald",Arial,sans-serif;text-transform:uppercase}
  .name-box__small{font-size:10px;color:#e2333d}
  .name-box__big{font-size:21px;color:var(--white);font-weight:500;line-height:1.1;margin:6px 0}
  .back-left p{padding:0 14px;text-align:justify}

  .back-right{position:absolute;left:198px;top:232px;width:350px}
  .back-right__head{font-size:9.5px;font-weight:500;margin-bottom:8px}
  .numbered{list-style:none;margin-bottom:10px}
  .numbered li{display:flex;gap:10px;margin-bottom:6px;font-style:italic}
  .numbered__num{flex:none;width:13px;height:13px;border-radius:50%;background:var(--red);color:var(--white);font-style:normal;font-weight:700;font-size:8px;display:flex;align-items:center;justify-content:center;box-shadow:0 0 0 1.5px #e9c1c3}
  .highlight{font-size:8.6px;font-style:italic;font-weight:700;color:var(--navy);line-height:1.35}
  .highlight .red{color:var(--red)}
  .closing{position:absolute;left:280px;top:672px;width:262px;font-size:7.4px}
</style>
</head>
<body>

<!-- FRONT PAGE -->
<section class="page page--front">
  <div class="photo" role="img" aria-label="Photo of a smiling customer service agent wearing a headset"
       style="left:0;top:0;width:270px;height:300px;background:linear-gradient(160deg,#f4ece6 0%,#d9c3b5 45%,#5a3d33 100%)"></div>

  <svg class="swoosh" style="top:200px" height="120" viewBox="0 0 560 120" aria-hidden="true">
    <path d="M0 40 C140 120 380 120 560 30 L560 120 L0 120 Z" fill="#ffffff"/>
    <path d="M0 48 C150 118 380 112 560 36 L560 60 C380 126 150 130 0 80 Z" fill="#a5161f"/>
    <path d="M0 84 C160 132 390 124 560 64 L560 72 C390 132 160 140 0 92 Z" fill="#25225e"/>
  </svg>

  <div class="brand" style="left:318px;top:48px;font-size:22px">
    <span class="brand__dot"></span>Brightline Office Systems
  </div>

  <div class="front-title heading">
    <div class="front-title__lead">The differences between</div>
    <div class="front-title__box">Brightline Office Systems &amp; Others</div>
    <div class="front-title__sub">And the psychology of how<br>we arrived at our model.</div>
  </div>

  <div class="col col--left">
    <div class="section-head"><span class="section-head__mark"></span>
      <span class="section-head__text">One of the most frustrating things about service in the copier industry is expectations.</span></div>
    <ul class="bullets">
      <li>If you call in for service via the phone, when will someone take "ownership" of your problem?</li>
      <li>Even if the average on-site response time is 2-4 hours?</li>
    </ul>
    <p>The ownership of your problem does not transfer to the tech until the tech arrives.</p>

    <div class="section-head"><span class="section-head__mark"></span>
      <span class="section-head__text">Worse yet is when you place a service</span></div>
    <ul class="bullets">
      <li>When will someone call you and take ownership of your problem?</li>
      <li>Not just dispatch the call but take ownership of your problem?</li>
      <li>Have you ever filled out a form online requesting information or help then waited hours or even days for a response?</li>
    </ul>
    <p>At Brightline Office Systems, we took a long hard look at the traditional service model of the copier industry and discovered that the main issue with copier service was the expectations of transfer of ownership with regards to the actual problem. When we asked our customers what was most important, response time to take over ownership was 1st and response time to be on site was second.</p>
  </div>

  <div class="col col--right">
    <div class="right-intro">Understanding this new sociology of service, allowed us to change the game in regards to service.</div>
    <div class="date-banner">
      <div class="date-banner__top">In October of 2017,</div>
      <div class="date-banner__mid">We started answering online requests for service</div>
      <div class="date-banner__end">In less than 5 minutes!</div>
    </div>
    <div class="point"><span class="point__mark"></span>
      <p>In addition, we no longer use dispatchers or office personnel to be the first responders. Now we have 2nd level technicians responding to the initial request. This has been a huge success in ways that we didn't even expect. 1st, 40% of all service requests are solved over the phone or internet by the responding 2nd level tech.</p></div>
    <div class="point"><span class="point__mark"></span>
      <p>Secondly, when a 2nd level tech assesses the problem on the first call, he gives the user the expectation that he has taken ownership of the problem and the expectation of the exact ETA of when the tech will be on site.</p></div>
    <div class="point"><span class="point__mark"></span>
      <p>Lastly, since the first responder is a 2nd level tech, the onsite tech is much more informed on what parts to bring or what are to focus on first.</p></div>
    <div class="result">This has led to a very high first visit fix rate of 93.7% compared the industry average of just 68.4%.</div>
  </div>

  <svg class="swoosh" style="top:648px" height="77" viewBox="0 0 560 77" aria-hidden="true">
    <path d="M0 0 L262 0 C280 0 282 10 290 30 C298 50 305 60 330 60 L560 60 L560 77 L0 77 Z" fill="#25225e"/>
  </svg>
  <div class="footer-call" style="left:22px;top:664px">
    <span class="footer-call__label">Call us today!</span>
    <span class="footer-call__number">555-014-2290</span>
  </div>
</section>

<!-- BACK PAGE -->
<section class="page page--back">
  <div class="photo" role="img" aria-label="Photo of a smiling support agent with a headset at a bright office desk"
       style="left:0;top:0;width:560px;height:230px;background:linear-gradient(100deg,#e9eef2 0%,#cfdbe3 40%,#e8d4c8 70%,#6a4a3e 100%)"></div>

  <svg class="swoosh" style="top:60px" height="175" viewBox="0 0 560 175" aria-hidden="true">
    <path d="M0 60 C150 160 360 175 560 120 L560 175 L0 175 Z" fill="#ffffff"/>
    <path d="M0 20 C140 120 360 140 560 70 L560 118 C360 170 150 160 0 58 Z" fill="#25225e"/>
    <path d="M0 52 C150 150 360 168 560 112 L560 120 C360 176 150 160 0 62 Z" fill="#a5161f"/>
  </svg>

  <div class="back-left">
    <div class="back-left__head heading">
      <span class="l1">For conversations regarding our ability to service</span>
      <span class="l2">Anywhere in the US.</span>
    </div>
    <div class="name-box">
      <div class="name-box__small">We changed our name to</div>
      <div class="name-box__big">Brightline Office Systems</div>
      <div class="name-box__small">In March of 2016 to more accurately describe what we do and where we do it.</div>
    </div>
    <div class="brand" style="position:relative;justify-content:center;margin:26px 0 24px;font-size:14px">
      <span class="brand__dot"></span>Brightline Office Systems
    </div>
    <p>All Copier companies who provide sales and service all over the US do it the same flawed way. if they have a company that needs copiers and service in multiple states or cities will have to negotiate separate service contracts with other copier companies in each respective state or city.</p>
  </div>

  <div class="back-right">
    <div class="back-right__head heading red">There are three major problems with doing so.</div>
    <ol class="numbered">
      <li><span class="numbered__num">1</span><p>Not all copier companies offer the same level of service in regards to response times, friendliness or quality of repairs. It varies greatly from state to state and city to city and there is very little command and control from the home copier company if something does not go well.</p></li>
      <li><span class="numbered__num">2</span><p>Conflicting Incentives of priorities. The local copier company will almost always service their own customers first when resources are strained. They do so because of the value of their own customers are much higher than their contracted accounts.</p></li>
      <li><span class="numbered__num">3</span><p>Service history data is fractured. Service history is actionable data that is important in the relationship between the copier vendor and the customer. In order to make changes in service, fleet size or redistributing resources, the service history is a vital tool.</p></li>
    </ol>
    <div class="back-right__head heading" style="margin-bottom:10px"><span class="red">At Brightline Office Systems, we worked for almost three years to solve this problem.</span><br><span class="navy">We solved this problem by doing the following.</span></div>
    <ol class="numbered">
      <li><span class="numbered__num">1</span><p>We eliminated the need to create separate side contracts with other copier companies by accumulating a vast database of contracted freelance copier technicians AND IT technicians.</p></li>
      <li><span class="numbered__num">2</span><p>We then created a program where the freelance techs wear a Brightline Office Systems shirt when performing Brightline Office Systems repairs.</p></li>
      <li><span class="numbered__num">3</span><p>The contracted tech is vetted and trained by Brightline Office Systems to a minimum service quality level.</p></li>
      <li><span class="numbered__num">4</span><p>Most importantly, all of our customers nationwide receive the same 5 minute response time on the transfer of ownership of their problem.</p></li>
      <li><span class="numbered__num">5</span><p>Command and control of all tech and service calls are retained by Brightline Office Systems nationwide!</p></li>
    </ol>
    <p class="highlight">One of the biggest advantages of developing this model is that our concentration of contracted freelance techs for any zip code is at least <span class="red">5-1</span> over the local vendor. <span class="red">For example,</span> any single copier company in Jacksonville Florida might have 2-3 technicians available at any given time. <span class="red">Brightline Office Systems has 26 contracted technicians</span> in a 25-mile radius of Jacksonville Florida.</p>
  </div>

  <svg class="swoosh" style="top:640px" height="85" viewBox="0 0 560 85" aria-hidden="true">
    <path d="M0 20 L200 20 C240 20 245 30 255 50 C262 64 268 75 300 75 L560 75 L560 85 L0 85 Z" fill="#25225e"/>
  </svg>
  <div class="footer-call" style="left:22px;top:672px">
    <span class="footer-call__label">Call us today!</span>
    <span class="footer-call__number">555-014-2290</span>
  </div>
  <p class="closing">This is a much more efficient, and properly incented service delivery model. It is a very disruptive methodology for delivering a kind of service experience that has not changed in 50 years.</p>
</section>

</body>
</html>
```